Family business needs stationery redesign with new logo

Family owned company, established in 1987 wanting a brand 'refresh'. We are an electrical, refrigeration and construction company based in the Barkly Region Northern Territory, Australia. We have a new logo we would like to use which is uploaded along with our current letterhead and email signature. We are also dropping the word 'contractors' so please do not include this on any designs. Please note also, the 'orange' color used in our logo and designs should be Northern Territory red ochre which is as follows:

RGB (Hex): #C75B12
PantoneĀ® 159 C
CMYK: 1 / 74 / 100 / 7

We are needing our stationery redesigned using our new logo. Please include letterheads, business cards, envelopes, and email signatures.

We currently use our business letterheads for quotations, invoices, letters, HR matters, and internal memos.

We also need a separate simplified letterhead for internal paperwork such as employee leave forms, meeting agendas, and meeting minutes etc.
Updates

Reason: Needing more submissions of full package designs. We are wanting all our stationery, including business cards, letterheads, email signatures, envelopes, etc to be cohesive. We also require ALL the information, as supplied on our template letterhead, to be included on the new letterhead designs. including electrical license no.etc Thank you, K&W

Reason: needing more time as work has got in the way of looking over designs. A lot of designs not meeting the brief/criteria.

Industry/Entity Type

Business

Colors
0355a3
f37122

Requirements
Must have
• The 'orange' color used in the designs should be Northern Territory red ochre which is as follows:
• RGB (Hex): #C75B12
• PantoneĀ® 159 C
• CMYK: 1 / 74 / 100 / 7
• ***MUST INCLUDE ALL INFORMATION THAT IS ON OUR CURRENT LETTERHEAD***
Should not have
• Please do not include the word 'contractors'

```html
<!DOCTYPE html>
<html lang="en">
<head>
<meta charset="utf-8">
<title>K&amp;W Email Signature</title>
<link rel="stylesheet" href="https://fonts.googleapis.com/css2?family=Montserrat:wght@400;500;700&display=swap">
<style>
  :root {
    --navy: #1b3270;
    --ochre: #c75b12;
    --ink: #1a1a1a;
    --paper: #ffffff;
  }
  html, body {
    margin: 0;
    padding: 0;
    overflow: hidden;
  }
  body {
    width: 1200px;
    height: 645px;
    background: var(--paper);
    font-family: "Montserrat", sans-serif;
    color: var(--ink);
  }
  .signature {
    position: relative;
    width: 1200px;
    height: 645px;
  }
  .brand {
    position: absolute;
    left: 100px;
    top: 253px;
    width: 286px;
    height: 138px;
    display: flex;
    align-items: center;
    justify-content: center;
    gap: 14px;
  }
  .brand-dot {
    width: 26px;
    height: 26px;
    border-radius: 50%;
    background: var(--ochre);
  }
  .brand-name {
    font-family: "Montserrat", sans-serif;
    font-weight: 700;
    font-size: 76px;
    line-height: 1;
    color: var(--navy);
  }
  .rule {
    position: absolute;
    left: 414px;
    top: 238px;
    width: 3px;
    height: 168px;
    background: var(--ochre);
  }
  .details {
    position: absolute;
    left: 433px;
    top: 244px;
  }
  .row {
    display: flex;
    align-items: center;
    height: 28px;
    font-size: 21px;
    font-weight: 400;
    white-space: nowrap;
  }
  .person-name {
    color: var(--navy);
    font-weight: 500;
    font-size: 22px;
  }
  .row.contact-numbers { margin-top: 8px; }
  .sep {
    display: inline-block;
    width: 1.5px;
    height: 27px;
    background: var(--ochre);
    margin: 0 7px;
  }
  .icon {
    width: 18px;
    height: 18px;
    margin-right: 10px;
    fill: var(--navy);
    flex: none;
  }
</style>
</head>
<body>
<div class="signature">
  <div class="brand">
    <span class="brand-name">K&amp;W</span>
    <span class="brand-dot"></span>
  </div>

  <div class="rule"></div>

  <div class="details">
    <div class="row person-name">Daniel Hart</div>
    <div class="row">Corporate Services Manager<span class="sep"></span>K&amp;W</div>
    <div class="row">
      <svg class="icon" viewBox="0 0 24 24"><path d="M12 1a8 8 0 0 0-8 8c0 6 8 14 8 14s8-8 8-14a8 8 0 0 0-8-8zm0 11a3 3 0 1 1 0-6 3 3 0 0 1 0 6z"/></svg>
      PO Box 4410<span class="sep"></span>52 Ridge Rd, Marlow Creek NT 0870
    </div>
    <div class="row contact-numbers">
      <svg class="icon" viewBox="0 0 24 24"><circle cx="12" cy="12" r="11"/><path fill="#fff" d="M8 6l2.5 0 1 3-1.5 1.2a8 8 0 0 0 3.8 3.8L15 12.5l3 1V16c0 1-1 2-2 2A10 10 0 0 1 6 8c0-1 1-2 2-2z"/></svg>
      08 8100 0000<span class="sep"></span>
      <svg class="icon" viewBox="0 0 24 24"><path d="M7 1h10a2 2 0 0 1 2 2v18a2 2 0 0 1-2 2H7a2 2 0 0 1-2-2V3a2 2 0 0 1 2-2zm0 3v14h10V4zm5 15.5a1.2 1.2 0 1 0 0 2.4 1.2 1.2 0 0 0 0-2.4z"/></svg>
      0400 000 000<span class="sep"></span>
      <svg class="icon" viewBox="0 0 24 24"><path d="M6 2h12v5H6zM3 8h18a2 2 0 0 1 2 2v7h-4v5H5v-5H1v-7a2 2 0 0 1 2-2zm4 7v5h10v-5zm2 1h6v1H9zm0 2h6v1H9z"/></svg>
      08 8100 0000
    </div>
    <div class="row">
      <svg class="icon" viewBox="0 0 24 24"><path d="M1 5h22v14H1zm2 2v.5l9 6 9-6V7zm0 3v7h18v-7l-9 6z"/></svg>
      Name@kwbuilds.com.au<span class="sep"></span>
      <svg class="icon" viewBox="0 0 24 24"><circle cx="12" cy="12" r="11"/><path fill="#fff" d="M12 3a9 9 0 0 0-6 2.5L8 9l3 1 1 3-2 2 1 5a9 9 0 0 0 2 .1l1-4 3-2-1-3h-3l-1-2 2-1 2-3a9 9 0 0 0-3-2z"/></svg>
      www.kwbuilds.com.au
    </div>
  </div>
</div>
</body>
</html>
```